Velorin Banner Design

We need banners for new company Velorin Holdings Limited located in Hong Kong. Velorin is an global online business platform, needs clean white, blue and red color mix banners.

Reason: I am extending for final design

Target Market(s)

Velorin an online Business Company have a target home based business owners and DIY website seekers.

Industry/Entity Type

Business

Colors
0355a3
ec2027
ffffff

Requirements
Must have
• Free Sign Up Button and Velorin Logo

```html
<!DOCTYPE html>
<html lang="en">
<head>
<meta charset="utf-8">
<title>Velorin Banner Set</title>
<link rel="stylesheet" href="https://fonts.googleapis.com/css2?family=Open+Sans:wdth,wght@75..100,600;75..100,700;75..100,800&display=swap">
<style>
:root{
  --blue:#0355a3;
  --blue-deep:#023f7d;
  --blue-light:#1a77c9;
  --red:#ec2027;
  --red-dark:#b8141a;
  --white:#ffffff;
  --logo-grey:#7d7f82;
  --stage:#e6e4e1;
  --shot-a:#dfe8f2;
  --shot-b:#2a5ea8;
}
*{box-sizing:border-box;margin:0;padding:0}
html,body{width:1200px;height:900px;overflow:hidden}
body{background:var(--stage);font-family:"Open Sans",Arial,sans-serif;position:relative;color:var(--white)}
.banner{position:absolute;overflow:hidden;background:linear-gradient(180deg,var(--blue-light) 0%,var(--blue) 45%,var(--blue-deep) 100%);box-shadow:0 3px 8px rgba(0,0,0,.35);border:1px solid #0a3566}
.banner .curve{position:absolute;left:0;width:100%;display:block}
.logo{position:absolute;display:flex;align-items:center;justify-content:center;gap:.3em;color:var(--logo-grey);font-weight:800;letter-spacing:.02em;font-stretch:90%;white-space:nowrap}
.logo .dot{width:.6em;height:.6em;border-radius:50%;background:var(--blue);flex:none}
.headline,.pitch{position:absolute;text-align:center;font-weight:700;line-height:1.15;font-stretch:88%}
.pitch{text-transform:uppercase}
.site-preview{position:absolute;border-radius:3px;background:linear-gradient(180deg,var(--shot-a) 0%,var(--shot-a) 18%,var(--shot-b) 19%,#3d7cc8 70%,#e9eef4 71%);border:2px solid #f4f6f8;box-shadow:0 4px 8px rgba(0,0,0,.35)}
.signup{position:absolute;display:flex;align-items:center;justify-content:center;border-radius:4px;background:linear-gradient(180deg,#ff5a5f 0%,var(--red) 45%,var(--red-dark) 100%);color:var(--white);font-weight:700;font-stretch:90%;box-shadow:0 2px 4px rgba(0,0,0,.35);white-space:nowrap}
.white-band{position:absolute;background:var(--white)}
</style>
</head>
<body>

<section class="banner skyscraper" style="left:181px;top:91px;width:186px;height:700px">
  <svg class="curve" style="top:0;height:62px" viewBox="0 0 186 62" preserveAspectRatio="none"><path d="M0 0H186V50Q93 68 0 50Z" fill="#fff"/></svg>
  <div class="logo" style="left:0;top:14px;width:186px;font-size:26px">VELORIN<span class="dot"></span></div>
  <h2 class="headline" style="left:0;top:80px;width:186px;font-size:26px;line-height:1.5">eCommerce<br>Website<br>$10/ Month</h2>
  <div class="site-preview" role="img" aria-label="Stacked screenshots of sample online store websites" style="left:-6px;top:220px;width:190px;height:160px"></div>
  <p class="pitch" style="left:0;top:448px;width:186px;font-size:16px">Revolutionary</p>
  <p class="pitch" style="left:0;top:472px;width:186px;font-size:23px">Single Line<br>Affiliate<br>Program</p>
  <svg class="curve" style="bottom:0;height:90px" viewBox="0 0 186 90" preserveAspectRatio="none"><path d="M0 14Q93 -4 186 14V90H0Z" fill="#fff"/></svg>
  <a class="signup" style="left:13px;top:637px;width:160px;height:42px;font-size:21px">Sign Up Free</a>
</section>

<section class="banner leaderboard" style="left:459px;top:90px;width:548px;height:70px">
  <div class="site-preview" role="img" aria-label="Screenshot of a sample online store website" style="left:12px;top:6px;width:100px;height:62px"></div>
  <h2 class="headline" style="left:118px;top:8px;width:316px;font-size:18px">eCommerce Website $10/ Month</h2>
  <p class="pitch" style="left:118px;top:30px;width:316px;font-size:13px;line-height:1.2">Revolutionary Single Line<br>Affiliate Program</p>
  <div class="white-band" style="left:432px;top:0;width:116px;height:70px"></div>
  <div class="logo" style="left:432px;top:8px;width:116px;font-size:17px">VELORIN<span class="dot"></span></div>
  <a class="signup" style="left:440px;top:36px;width:102px;height:26px;font-size:13px">Sign Up Free</a>
</section>

<section class="banner small-square" style="left:465px;top:219px;width:140px;height:187px">
  <div class="white-band" style="left:0;top:0;width:140px;height:22px"></div>
  <div class="logo" style="left:0;top:2px;width:140px;font-size:15px">VELORIN<span class="dot"></span></div>
  <h2 class="headline" style="left:0;top:25px;width:140px;font-size:12px;text-transform:uppercase">eCommerce Website<br>$10/ Month</h2>
  <div class="site-preview" role="img" aria-label="Screenshot of a sample online store website" style="left:30px;top:56px;width:94px;height:64px"></div>
  <p class="pitch" style="left:0;top:124px;width:140px;font-size:11px">Revolutionary<br>Single Line<br>Affiliate Program</p>
  <a class="signup" style="left:12px;top:164px;width:116px;height:19px;font-size:12px">Sign Up Free</a>
</section>

<section class="banner medium-rectangle" style="left:715px;top:260px;width:290px;height:291px">
  <svg class="curve" style="top:0;height:46px" viewBox="0 0 290 46" preserveAspectRatio="none"><path d="M0 0H290V36Q145 52 0 36Z" fill="#fff"/></svg>
  <div class="logo" style="left:0;top:8px;width:290px;font-size:25px">VELORIN<span class="dot"></span></div>
  <h2 class="headline" style="left:0;top:53px;width:290px;font-size:21px;line-height:1.05">eCommerce Website<br>$10/ Month</h2>
  <div class="site-preview" role="img" aria-label="Screenshot of a sample online store website" style="left:10px;top:100px;width:154px;height:112px"></div>
  <p class="pitch" style="left:174px;top:125px;width:110px;font-size:12px;text-align:left">Revolutionary</p>
  <p class="pitch" style="left:174px;top:141px;width:110px;font-size:17px;text-align:left;line-height:1.1">Single Line<br>Affiliate<br>Program</p>
  <svg class="curve" style="bottom:0;height:70px" viewBox="0 0 290 70" preserveAspectRatio="none"><path d="M0 8Q145 -8 290 8V70H0Z" fill="#fff"/></svg>
  <a class="signup" style="left:57px;top:244px;width:176px;height:36px;font-size:19px">Sign Up Free</a>
</section>

<section class="banner small-banner" style="left:465px;top:464px;width:140px;height:106px">
  <h2 class="headline" style="left:0;top:3px;width:140px;font-size:12px;line-height:1.1">eCommerce Website<br>$10/ Month</h2>
  <div class="site-preview" role="img" aria-label="Screenshot of a sample online store website" style="left:3px;top:36px;width:58px;height:44px"></div>
  <p class="pitch" style="left:62px;top:31px;width:72px;font-size:9px;line-height:1.2;text-align:right;font-stretch:80%">Revolutionary<br>Single Line<br>Affiliate<br>Program</p>
  <div class="white-band" style="left:0;top:86px;width:140px;height:20px"></div>
  <div class="logo" style="left:2px;top:87px;width:64px;height:18px;font-size:11px;gap:.25em">VELORIN<span class="dot"></span></div>
  <a class="signup" style="left:72px;top:87px;width:68px;height:18px;font-size:10px;border-radius:0">Sign Up Free</a>
</section>

<section class="banner square" style="left:459px;top:645px;width:146px;height:148px">
  <svg class="curve" style="top:0;height:20px" viewBox="0 0 146 20" preserveAspectRatio="none"><path d="M0 0H146V15Q73 22 0 15Z" fill="#fff"/></svg>
  <div class="logo" style="left:0;top:1px;width:146px;font-size:12px">VELORIN<span class="dot"></span></div>
  <h2 class="headline" style="left:0;top:21px;width:146px;font-size:12px;line-height:1.1">eCommerce Website<br>$10/ Month</h2>
  <div class="site-preview" role="img" aria-label="Screenshot of a sample online store website" style="left:4px;top:68px;width:58px;height:44px"></div>
  <p class="pitch" style="left:60px;top:52px;width:78px;font-size:10px;line-height:1.25;text-align:right;font-stretch:82%">Revolutionary<br>Single Line<br>Affiliate<br>Program</p>
  <div class="white-band" style="left:0;top:122px;width:146px;height:26px"></div>
  <a class="signup" style="left:26px;top:124px;width:94px;height:19px;font-size:11px">Sign Up Free</a>
</section>

</body>
</html>
```